Brisa Home Residential cleaning services- Opening Flyer

1. I would like to have flyer design offering the hourly rate residential cleaning normal rate will be 35 AED per hour.
2. I want to have a special opening rate which is less than 25 AED which is equivalent to 30% Off.This opening offer will be limited time
We have a different cleaning packages like "Basic , Deep, And custom"
3. Also we have different types contracts Yearly/Monthly/Weekly and daily.
4. we are providing cleaning material and cleaning equipment upon request.And all the material used are environmental friendly.
5. Our customers mostly will be house wives.
6. Our service will be available in Ruwais city.
7. I would like to have a modern attractive flyer, i like it to be smart in its colors and the psychology of the customers.
8. I like to have attractive statements like " Now Available in Ruwais" and other statements from your own.
9. I will attach my logo design and if you need any other uploads let me know.
10. Our slogan is "Experience the Difference"
11. Paper size , i expect to be A5 (210mm x 148mm).
12. I am expecting the flyer to be single size as it will translated to another language in the other side.
13. please use the statement also ( less than 25 AED)
14. Do the arrangement you can see to the flyer statements as to look professional and comfortable to read.
15. Company web site is " www.brisahome.ae"
16. company email " support@brisahome.ae"
17. I will update you with contact number soon
18. My contacts are
Support@brisahome.ae
+971 508817394
+971 508817396
19. Update some slogans to be used
Industry/Entity Type
Residential
Look and feel
Each slider illustrates characteristics of the customer's brand and the style your logo design should communicate.

```html
<!DOCTYPE html>
<html lang="en">
<head>
<meta charset="utf-8">
<title>Brisa Home – Residential Cleaning Flyer</title>
<link rel="stylesheet" href="https://fonts.googleapis.com/css2?family=Open+Sans:wght@400;600;700&family=Roboto:wght@300;400&family=Roboto+Condensed:wght@400&display=swap">
<style>
  :root {
    --lime: #a6cf38;
    --lime-text: #9ccb3b;
    --sky: #2aa3e0;
    --navy: #1a5fa8;
    --ink: #1b1b1b;
    --grey-text: #8a8a8a;
    --band-grey: #e6e7e8;
    --white: #ffffff;
  }
  * { margin: 0; padding: 0; box-sizing: border-box; }
  html, body { width: 893px; height: 1200px; overflow: hidden; background: var(--white); }
  .flyer { position: relative; width: 893px; height: 1200px; background: var(--white); font-family: "Open Sans", sans-serif; }

  .slogan-bar {
    position: absolute; left: 0; top: 0; width: 893px; height: 123px;
    background: var(--lime); color: var(--white);
    display: flex; align-items: center; justify-content: center;
    font-weight: 700; font-size: 50px; letter-spacing: 0.3px;
  }

  .hero { position: absolute; left: 0; top: 134px; width: 893px; height: 640px; }

  .brand-name {
    position: absolute; left: 205px; top: 628px;
    font-family: "Open Sans", sans-serif; font-weight: 700; font-size: 64px; line-height: 1;
    color: var(--white); letter-spacing: -1px;
  }

  .services-title {
    position: absolute; left: 41px; top: 768px;
    font-family: "Roboto", sans-serif; font-weight: 400; font-size: 28px; color: var(--navy);
  }
  .feature { position: absolute; left: 40px; }
  .feature .tick { position: absolute; left: 0; top: 4px; width: 34px; height: 34px; }
  .feature h3 { margin-left: 52px; font-weight: 700; color: var(--lime-text); font-size: 35px; line-height: 1.1; }
  .feature p { margin-left: 56px; font-family: "Roboto", sans-serif; font-weight: 300; color: var(--grey-text); }
  .feature.contracts { top: 824px; }
  .feature.contracts p { font-size: 27px; margin-top: 6px; }
  .feature.packages { top: 916px; }
  .feature.packages p { font-size: 21px; margin-top: 4px; }

  .offer {
    position: absolute; left: 577px; top: 803px; width: 283px; height: 191px;
    background: var(--navy); border-radius: 20px; padding: 8px;
  }
  .offer-inner {
    width: 100%; height: 100%; border: 2px solid var(--white); border-radius: 14px;
    display: flex; flex-direction: column; align-items: center; justify-content: center;
    color: var(--white); font-family: "Roboto", sans-serif; text-align: center;
  }
  .offer-label { font-size: 19px; line-height: 1.35; }
  .offer-amount { color: var(--lime); font-family: "Open Sans", sans-serif; font-weight: 600; font-size: 60px; line-height: 1.1; }
  .offer-amount small { font-size: 40px; font-weight: 700; }
  .offer-note { font-size: 24px; margin-top: 2px; }

  .info-band {
    position: absolute; left: 0; top: 1019px; width: 893px; height: 157px; background: var(--band-grey);
  }
  .about {
    position: absolute; left: 41px; top: 30px; width: 460px;
    font-family: "Roboto Condensed", sans-serif; font-size: 20px; line-height: 34px; color: var(--ink);
  }
  .contact { position: absolute; left: 528px; top: 28px; width: 340px; }
  .contact .cta { font-size: 24px; color: var(--navy); line-height: 1.2; }
  .phone-line { display: flex; align-items: center; margin-top: 6px; }
  .phone-line svg { width: 46px; height: 52px; margin-right: 10px; }
  .phone-line span { font-family: "Roboto Condensed", sans-serif; font-weight: 700; font-size: 42px; color: #000; letter-spacing: 0.5px; }
  .contact .web { margin-left: 56px; font-size: 28px; color: var(--navy); line-height: 1.2; }

  .bottom-bar { position: absolute; left: 0; top: 1176px; width: 893px; height: 24px; background: var(--lime); }
</style>
</head>
<body>
<div class="flyer">
  <header class="slogan-bar">Experience the Difference</header>

  <svg class="hero" viewBox="0 0 893 640" xmlns="http://www.w3.org/2000/svg">
    <defs>
      <linearGradient id="kitchenTone" x1="0" y1="0" x2="1" y2="1">
        <stop offset="0" stop-color="#e9ecef"/>
        <stop offset="0.45" stop-color="#c9cdd1"/>
        <stop offset="1" stop-color="#eef0ea"/>
      </linearGradient>
      <linearGradient id="swoosh" x1="0" y1="0" x2="1" y2="0">
        <stop offset="0" stop-color="#8fd0f2"/>
        <stop offset="0.25" stop-color="#2aa3e0"/>
        <stop offset="1" stop-color="#2aa3e0"/>
      </linearGradient>
    </defs>
    <rect role="img" aria-label="Smiling woman in yellow gloves cleaning a bright kitchen counter with a spray bottle" x="0" y="0" width="893" height="600" fill="url(#kitchenTone)"/>
    <path d="M893,332 C820,470 700,560 470,640 L893,640 Z" fill="#ffffff"/>
    <path d="M0,640 L0,612 C260,620 520,590 700,520 C770,565 800,500 800,450 C760,480 700,500 620,508 C420,525 180,470 0,340 Z" fill="url(#swoosh)" transform="translate(0,0)"/>
    <path d="M0,640 L0,612 C260,620 520,590 700,520 L893,520 L893,640 Z" fill="#ffffff"/>
    <circle cx="680" cy="514" r="92" fill="#ffffff" stroke="#a6cf38" stroke-width="5"/>
  </svg>

  <div class="brand-name">Brisa Home</div>

  <h2 class="services-title">RESIDENTIAL CLEANING SERVICES</h2>

  <div class="feature contracts">
    <svg class="tick" viewBox="0 0 34 34"><path d="M3,19 L12,29 L31,3" fill="none" stroke="#9ccb3b" stroke-width="3" stroke-linecap="round"/></svg>
    <h3>Different Types Contracts</h3>
    <p>Yearly &nbsp;•&nbsp; Monthly &nbsp;•&nbsp; Weekly &nbsp;•&nbsp; Daily</p>
  </div>

  <div class="feature packages">
    <svg class="tick" viewBox="0 0 34 34"><path d="M3,19 L12,29 L31,3" fill="none" stroke="#9ccb3b" stroke-width="3" stroke-linecap="round"/></svg>
    <h3>Cleaning Packages</h3>
    <p>Basic &nbsp;•&nbsp; Deep &nbsp;•&nbsp; Custom</p>
  </div>

  <aside class="offer">
    <div class="offer-inner">
      <div class="offer-label">SPECIAL<br>OPENING OFFER</div>
      <div class="offer-amount">30% <small>off</small></div>
      <div class="offer-note">less than 25 AED</div>
    </div>
  </aside>

  <footer class="info-band">
    <p class="about">Brisa Home cleaning company offers high-quality<br>home cleaning services.<br>All the material used are&nbsp; environmental friendly.</p>
    <div class="contact">
      <div class="cta">Call today for a Free Estimate!</div>
      <div class="phone-line">
        <svg viewBox="0 0 46 52"><path d="M30,4 C12,6 6,20 12,32 L4,32 L20,50 L34,32 L24,32 C20,22 22,12 32,8 Z" fill="#1a5fa8"/></svg>
        <span>000 0000 0000</span>
      </div>
      <div class="web">www.brisahome.ae</div>
    </div>
  </footer>
  <div class="bottom-bar"></div>
</div>
</body>
</html>
```